Business card design for Tolbrin Waste

I would like double-sided business cards for myself and my partner that includes our logo and the existing colour scheme. We provide waste and environmental services to customers in the motor-vehicle and engineering industries.

```html
<!DOCTYPE html>
<html lang="en">
<head>
<meta charset="utf-8">
<title>Tolbrin Waste – Business Card</title>
<link rel="stylesheet" href="https://fonts.googleapis.com/css2?family=Roboto:wght@400;500;700&display=swap">
<style>
  :root {
    --backdrop: #3a3a3a;
    --brand-green: #78ad3a;
    --light-green: #9cc63f;
    --ink: #4a4a4a;
    --paper: #ffffff;
    --faint-green: #eef4e4;
  }
  * { box-sizing: border-box; margin: 0; padding: 0; }
  html, body { width: 1200px; height: 960px; overflow: hidden; }
  body {
    background: var(--backdrop);
    font-family: "Roboto", sans-serif;
    position: relative;
  }
  .card {
    position: absolute;
    left: 215px;
    width: 770px;
    height: 440px;
    overflow: hidden;
  }
  .card--front { top: 25px; background: var(--brand-green); }
  .card--back { top: 495px; background: var(--paper); }

  .front-brand {
    position: absolute;
    right: 60px;
    bottom: 70px;
    text-align: right;
    color: var(--paper);
  }
  .front-brand .brand-name {
    font-size: 52px;
    font-weight: 700;
    letter-spacing: 1px;
    text-transform: uppercase;
    line-height: 1;
  }
  .front-brand .brand-url {
    margin-top: 14px;
    font-size: 15px;
    letter-spacing: 4px;
  }

  .back-brand {
    position: absolute;
    left: 60px;
    top: 70px;
    display: flex;
    align-items: center;
    gap: 16px;
  }
  .back-brand .brand-dot {
    width: 58px; height: 58px;
    border-radius: 50%;
    background: var(--light-green);
  }
  .back-brand .brand-name {
    font-size: 40px;
    font-weight: 700;
    text-transform: uppercase;
    color: var(--ink);
    letter-spacing: 1px;
  }

  .address {
    position: absolute;
    left: 60px;
    top: 200px;
    font-size: 17px;
    line-height: 22px;
    color: var(--ink);
  }
  .contacts {
    position: absolute;
    left: 60px;
    top: 262px;
    list-style: none;
    font-size: 17px;
    color: var(--ink);
  }
  .contacts li {
    display: flex;
    align-items: center;
    gap: 10px;
    height: 25px;
  }
  .contacts svg { width: 16px; height: 16px; fill: var(--brand-green); flex: none; }

  .decor-ring {
    position: absolute;
    right: -40px;
    top: 20px;
    width: 300px;
    height: 300px;
    border-radius: 50%;
    border: 22px solid var(--faint-green);
  }
  .holder {
    position: absolute;
    right: 70px;
    top: 150px;
    text-align: right;
  }
  .holder .holder-name {
    font-size: 26px;
    font-weight: 500;
    color: var(--brand-green);
    text-transform: uppercase;
  }
  .holder .holder-role {
    font-size: 17px;
    color: var(--light-green);
    text-transform: uppercase;
  }
  .edge-tab {
    position: absolute;
    right: 0;
    top: 150px;
    width: 48px;
    height: 30px;
    background: var(--brand-green);
  }
</style>
</head>
<body>
  <section class="card card--front">
    <div class="front-brand">
      <div class="brand-name">Tolbrin Waste</div>
      <div class="brand-url">www.tolbrinwaste.com</div>
    </div>
  </section>

  <section class="card card--back">
    <div class="decor-ring"></div>
    <div class="back-brand">
      <span class="brand-dot"></span>
      <span class="brand-name">Tolbrin Waste</span>
    </div>

    <p class="address">214 Alder Row<br>Juneau, Alaska 34610</p>

    <ul class="contacts">
      <li><svg viewBox="0 0 16 16"><path d="M3 1l3 3-1.5 2a9 9 0 0 0 5.5 5.5L12 10l3 3-2 2C7 15 1 9 1 3z"/></svg>555 214 0387</li>
      <li><svg viewBox="0 0 16 16"><path d="M4 0h8v16H4zM5.5 2v10h5V2z"/></svg>555 730 1926</li>
      <li><svg viewBox="0 0 16 16"><path d="M4 1h7v4H4zM1 6h14v8H1zm3 2v2h8V8z"/></svg>555 468 2051</li>
      <li><svg viewBox="0 0 16 16"><path d="M0 3h16v10H0zm1.5 1.5L8 9l6.5-4.5z"/></svg>marten@tolbrinwaste.com</li>
      <li><svg viewBox="0 0 16 16"><circle cx="8" cy="8" r="8"/></svg>www.tolbrinwaste.com</li>
    </ul>

    <div class="edge-tab"></div>
    <div class="holder">
      <div class="holder-name">Marten Hale</div>
      <div class="holder-role">CEO/Founder</div>
    </div>
  </section>
</body>
</html>
```